EPS Recycling End Market Infographic

We need a two-page visual presentation of new end-market applications for recycled expanded polystyrene (EPS) collected for recycling. This focuses on expanded polystyrene (foam) transport packaging used for international distribution of goods, including pharmaceuticals and food, electronics, appliances and other products that need superior packaging protection.

The bulletin will have examples of 5 major industry categories that benefit from recycled EPS feedstock for reverse engineering to meet current market demand. It will also showcase names of companies that use recycled content EPS in their product manufacturing to legitimize end market adoption. The capability to use recycled EPS in new EPS packaging should be highlighted. We would like this bulletin to demonstrate the widespread application of recycled EPS in different industries and establish credibility that it is being used in a variety of interesting recycled-content products. We welcome creative and interesting font treatments and new trends in graphic design.

Target Market(s)

International Government Agencies, Packaging Engineers, Big Box Retailers, & Environmental Professionals

Industry/Entity Type

Plastic Manufacturers

Font styles to use
Sans Serif

Requirements
Must have
• Visual focus points, multiple examples of products and manufacturers as evidence to the information content
Should not have
• Insufficient white space or outdated design elements (like two-tone gradients).

```html
<!DOCTYPE html>
<html lang="en">
<head>
<meta charset="utf-8">
<title>Recycled EPS End Markets</title>
<link href="https://fonts.googleapis.com/css2?family=Roboto+Condensed:wght@300;400;700&family=Roboto:wght@400;500;700&family=Montserrat:ital,wght@1,500&display=swap" rel="stylesheet">
<style>
:root{
  --bg:#d6d6d6;
  --green:#a3a93c;
  --orange:#f7a11f;
  --blue:#5f8ea8;
  --brown:#5c2e1e;
  --tan:#b8892f;
  --ink:#1e1e1e;
  --panel:#f2f3f7;
  --white:#ffffff;
}
*{margin:0;padding:0;box-sizing:border-box}
html,body{width:800px;height:1200px;overflow:hidden;background:var(--bg)}
body{position:relative;font-family:"Roboto",Arial,sans-serif;color:var(--ink)}
.abs{position:absolute}
.page{position:absolute;left:51px;width:699px;background:var(--white);box-shadow:1px 2px 3px rgba(0,0,0,.35)}
.page-one{top:37px;height:540px}
.page-two{top:603px;height:539px}
.band{position:absolute;left:0;width:100%;background:var(--green)}
.chevron{position:absolute;width:0;height:0;border-left:17px solid transparent;border-right:17px solid transparent}
.main-title{position:absolute;left:40px;top:20px;font-family:"Roboto Condensed",sans-serif;font-size:48px;color:var(--white);font-weight:300;letter-spacing:.5px;white-space:nowrap}
.main-title b{font-weight:700}
.intro{position:absolute;left:76px;top:120px;font-size:10.2px;line-height:13px;font-weight:500}
.market-panel{position:absolute;left:476px;top:176px;width:205px;height:347px;background:var(--panel)}
.market{position:absolute;left:518px;width:150px;font-size:7.6px;line-height:9.6px;color:#333}
.market h3{font-size:7.8px;font-weight:700;color:var(--ink);margin-bottom:1px}
.dot-back{position:absolute;width:31px;height:31px;border-radius:50%}
.photo-circle{position:absolute;width:48px;height:48px;border-radius:50%}
.cooler-photo{position:absolute;left:79px;top:193px;width:324px;height:247px;background:linear-gradient(180deg,#f4f5f3,#e4e6e3);clip-path:polygon(0 12%,100% 12%,100% 22%,90% 22%,82% 100%,20% 100%,8% 22%,0 22%)}
.stat{position:absolute;left:20px;top:310px;width:280px;border:3px solid var(--white)}
.stat-num{background:var(--green);height:57px;color:var(--white);font-family:"Roboto Condensed",sans-serif;font-weight:700;font-size:46px;line-height:57px;padding-left:25px}
.stat-num span{font-size:32px}
.stat-sub{background:var(--blue);height:45px;color:var(--white);font-family:"Roboto Condensed",sans-serif;font-weight:700;font-size:15px;line-height:16px;padding:7px 0 0 25px}
.stat-sub .spaced{letter-spacing:4.6px}
.cooler-label{position:absolute;left:125px;top:475px;font-family:"Montserrat",sans-serif;font-style:italic;font-weight:500;font-size:10.5px;letter-spacing:1.6px;color:var(--brown)}
.section-title{position:absolute;font-family:"Roboto Condensed",sans-serif;color:var(--white);font-weight:400;white-space:nowrap}
.section-title b{font-weight:700}
.product-img{position:absolute;top:70px;height:82px}
.tag{position:absolute;height:14px;color:var(--white);font-size:8.6px;font-weight:700;text-align:center;line-height:14px;white-space:nowrap}
.tag-tall{height:33px;line-height:11px;padding-top:5px}
.tag-tall small{display:block;font-size:7.5px;font-weight:400}
.maker{position:absolute;font-size:9px;text-align:center;color:#333}
.other-area{position:absolute;left:0;top:332px;width:100%;height:181px;background:var(--panel)}
.list-item{position:absolute;font-size:8.8px;font-weight:700;line-height:13px;color:#2a2a2a;white-space:nowrap}
.list-item::before{content:"";position:absolute;left:-11px;top:3px;width:5px;height:5px;border-radius:50%;background:var(--orange)}
.footer-text{position:absolute;left:0;width:100%;top:513px;height:26px;line-height:26px;text-align:center;color:var(--white);font-weight:700;font-size:13.5px}
</style>
</head>
<body>

<section class="page page-one">
  <div class="band" style="top:0;height:86px"></div>
  <div class="chevron" style="left:113px;top:86px;border-top:16px solid var(--green)"></div>
  <h1 class="main-title"><b>RECYCLED</b> EPS END MARKETS</h1>
  <p class="intro">Recycled eps foam can be repurposed into a diverse array of products across various industries.<br>These applications underscore the versatility of recycled eps, contributing to sustainability across multiple sectors.</p>

  <div class="cooler-photo" role="img" aria-label="Speckled white cooler made with recycled EPS content"></div>

  <div class="stat">
    <div class="stat-num">30,800 <span>TONS</span></div>
    <div class="stat-sub">OF EXPANDED POLYSTYRENE (EPS)<br><span class="spaced">WAS RECYCLED IN 2022</span></div>
  </div>

  <svg class="abs" style="left:0;top:0" width="699" height="540" aria-hidden="true">
    <path d="M250 446 Q180 480 102 421" fill="none" stroke="var(--green)" stroke-width="2.5" stroke-dasharray="8 5"/>
    <path d="M97 430 L101 419 L112 421" fill="none" stroke="var(--green)" stroke-width="2.5"/>
    <g stroke="var(--orange)" stroke-width="2.5" stroke-dasharray="2.5 2" fill="none">
      <line x1="416" y1="214" x2="416" y2="470"/>
      <line x1="416" y1="214" x2="441" y2="214"/>
      <line x1="416" y1="275" x2="441" y2="275"/>
      <line x1="310" y1="345" x2="441" y2="345"/>
      <line x1="416" y1="403" x2="441" y2="403"/>
      <line x1="416" y1="470" x2="441" y2="470"/>
    </g>
  </svg>

  <div class="market-panel"></div>

  <div class="dot-back" style="left:437px;top:202px;background:var(--green)"></div>
  <div class="photo-circle" style="left:452px;top:194px;background:linear-gradient(135deg,#6f9fce,#e9ecef)" role="img" aria-label="Modern building facade"></div>
  <div class="dot-back" style="left:437px;top:263px;background:var(--orange)"></div>
  <div class="photo-circle" style="left:452px;top:255px;background:linear-gradient(135deg,#a9aca6,#7e8278)" role="img" aria-label="Close-up of woven textile fibers"></div>
  <div class="dot-back" style="left:437px;top:326px;background:var(--blue)"></div>
  <div class="photo-circle" style="left:452px;top:318px;background:linear-gradient(135deg,#e0a33c,#b2701c)" role="img" aria-label="Wood composite chips"></div>
  <div class="dot-back" style="left:437px;top:387px;background:var(--brown)"></div>
  <div class="photo-circle" style="left:452px;top:379px;background:linear-gradient(135deg,#3f58c4,#1a2470)" role="img" aria-label="Swirl of blue paint"></div>
  <div class="dot-back" style="left:437px;top:448px;background:var(--tan)"></div>
  <div class="photo-circle" style="left:452px;top:440px;background:linear-gradient(135deg,#9a9a9a,#2c2c2c)" role="img" aria-label="3D printer machinery"></div>

  <div class="market" style="top:190px"><h3>Construction &amp; Architectural</h3>Walls, insulation, and geoforam are all products that can utilize recycled EPS as part of the design. Ground or shredded EPS can be mixed in with concrete or asphalt to improve quality.</div>
  <div class="market" style="top:259px"><h3>Textile &amp; Fiber</h3>Specialized techniques produce fine fibers of EPS to be used in non-woven mats and in nanofibers to help absorb oil spills.</div>
  <div class="market" style="top:317px"><h3>Wood Composites &amp; Blends</h3>Novel applications using EPS can avoid traditional glue use in wood composites by combining EPS with waste wood fibers.</div>
  <div class="market" style="top:376px"><h3>Paints, Coatings, Adhesives</h3>Water resistant paints are needed for architectural and roadway applications. EPS can be recycled into a resin and mixed into paint to enhance water resistance.</div>
  <div class="market" style="top:444px"><h3>Additives</h3>Modern approaches to plastics manufacturing can use recycled EPS to create material for 3D printing.</div>

  <div class="cooler-label">RECYCLED CONTENT EPS COOLER</div>
</section>

<section class="page page-two">
  <div class="band" style="top:0;height:38px"></div>
  <div class="chevron" style="left:113px;top:38px;border-top:19px solid var(--green)"></div>
  <h2 class="section-title" style="left:58px;top:3px;font-size:24px"><b>Products and Manufacturers</b> That Use EPS Recycled Content</h2>

  <div class="product-img" style="left:33px;width:110px;background:linear-gradient(180deg,#f7f7f7,#dcdcdc)" role="img" aria-label="White molded foam automotive component"></div>
  <div class="product-img" style="left:150px;width:102px;background:linear-gradient(180deg,#7ea3bd,#4f7895)" role="img" aria-label="Blue wooden-style patio bench"></div>
  <div class="product-img" style="left:278px;width:50px;background:linear-gradient(180deg,#555,#1f1f1f)" role="img" aria-label="Black plastic spoon"></div>
  <div class="product-img" style="left:340px;width:90px;top:96px;height:30px;background:linear-gradient(180deg,#f2f2f0,#d4d4d0)" role="img" aria-label="White surfboard blank"></div>
  <div class="product-img" style="left:463px;width:93px;background:linear-gradient(180deg,#a97b5a,#8a5f43)" role="img" aria-label="Brown clothing hangers"></div>
  <div class="product-img" style="left:589px;width:64px;background:linear-gradient(180deg,#d8c6ab,#b9a283)" role="img" aria-label="Beige picture frame"></div>

  <div class="tag" style="left:22px;top:162px;width:122px;background:var(--green)">AUTOMOTIVE COMPONENTS</div>
  <div class="tag" style="left:158px;top:162px;width:78px;background:var(--orange)">PATIO BENCH</div>
  <div class="tag" style="left:249px;top:162px;width:72px;background:var(--blue)">SPOON</div>
  <div class="tag" style="left:335px;top:162px;width:103px;background:var(--brown)">SURFBOARD BLANKS</div>
  <div class="tag" style="left:450px;top:162px;width:104px;background:var(--tan)">CLOTHING HANGERS</div>
  <div class="tag" style="left:568px;top:162px;width:104px;background:var(--blue)">PICTURE FRAME</div>

  <div class="maker" style="left:22px;top:178px;width:122px">By Norvell</div>
  <div class="maker" style="left:154px;top:178px;width:86px">BY Birchline</div>
  <div class="maker" style="left:243px;top:178px;width:84px">By Greenware Co.</div>
  <div class="maker" style="left:335px;top:178px;width:103px">BY Tidecraft Foam</div>
  <div class="maker" style="left:450px;top:178px;width:104px">BY Hangwell</div>
  <div class="maker" style="left:560px;top:178px;width:120px">BY Framewise Recycling</div>

  <div class="tag tag-tall" style="left:22px;top:226px;width:122px;background:var(--orange);padding-top:0;line-height:33px">LIGHTWEIGHT CONCRETE</div>
  <div class="tag tag-tall" style="left:158px;top:226px;width:81px;background:var(--brown);padding-top:0;line-height:33px">PAINT BINDERS</div>
  <div class="tag tag-tall" style="left:253px;top:226px;width:164px;background:var(--tan)">SPECIALTY WAXES &amp; POLYMERS<small>Used in: Roofing, Paving, Composites</small></div>
  <div class="tag tag-tall" style="left:430px;top:226px;width:125px;background:var(--blue)">INTERIOR MOLDINGS<small>Crown Molding, Base Board</small></div>
  <div class="tag tag-tall" style="left:569px;top:226px;width:104px;background:var(--green);padding-top:0;line-height:27px">BICYCLE HELMETS</div>

  <div class="maker" style="left:22px;top:263px;width:122px">By Cembloc</div>
  <div class="maker" style="left:158px;top:263px;width:81px">by Binderly</div>
  <div class="maker" style="left:253px;top:263px;width:164px">by Polyleaf</div>
  <div class="maker" style="left:430px;top:263px;width:125px">by Trimform</div>
  <div class="maker" style="left:569px;top:263px;width:104px">by Veloshell</div>

  <div class="band" style="top:307px;height:25px;background:var(--blue)"></div>
  <div class="other-area"></div>
  <div class="chevron" style="left:110px;top:332px;border-top:19px solid var(--blue)"></div>
  <h2 class="section-title" style="left:58px;top:310px;font-size:14.5px"><b>Other Examples of Products</b> That Use EPS Recycled Content</h2>

  <div class="list-item" style="left:67px;top:373px">LIGHTWEIGHT CONCRETE</div>
  <div class="list-item" style="left:67px;top:399px">INSULATION PANELS /BLOCKS</div>
  <div class="list-item" style="left:67px;top:424px">GEOFOAM &amp; SOIL IMPROVEMENT</div>
  <div class="list-item" style="left:67px;top:450px">NON-WOVEN FABRICS</div>
  <div class="list-item" style="left:228px;top:373px">FIBER ABSORBENTS</div>
  <div class="list-item" style="left:228px;top:399px">FILTERS</div>
  <div class="list-item" style="left:228px;top:424px">COMPOSITE BINDERS</div>
  <div class="list-item" style="left:228px;top:450px">GLUE</div>
  <div class="list-item" style="left:362px;top:373px">PROTECTIVE &amp; HYDROPHOBIC</div>
  <div class="list-item" style="left:362px;top:399px">COATINGS</div>
  <div class="list-item" style="left:362px;top:424px">ADHESIVES &amp; SEALANTS</div>
  <div class="list-item" style="left:362px;top:450px">3D PRINTING FILAMENTS</div>
  <div class="list-item" style="left:520px;top:373px">DIRECT INK WRITING</div>
  <div class="list-item" style="left:520px;top:401px">INJECTION MOLDING<br>&amp; EXTRUSION</div>

  <div class="band" style="top:513px;height:26px"></div>
  <div class="footer-text">Learn more at www.foamloop.org</div>
</section>

</body>
</html>
```